Incontinence A4 Posters

A variation of 2 different designs advertising a laser incontinence treatment to be place on the back of female toilet doors. We can supply some facts and statistics, must be simple and eye catching. Must Align with the aesthetic of an up market clinic. Have a look at our website laser vaginal rejuvenation page to see the look we are going for.
The treatment is performed with a Laser and tightens the vaginal walls to stop incontinence.
Design must include website company logo phone number and what the treatment is.
I have attached the company logo.

Target Market(s)

Females 30-60 years old. New mums and older ladies.

Industry/Entity Type

Advertising

Colors
ec1f27

Requirements
Must have
• Company logo. That the treatment is performed with a laser. website phone number contact details
Should not have
• Should not look tacky or cheap

```html
<!DOCTYPE html>
<html lang="en">
<head>
<meta charset="utf-8">
<title>Laser Vaginal Rejuvenation Poster</title>
<link href="https://fonts.googleapis.com/css2?family=Open+Sans:wght@400;600;700&family=Roboto+Slab:wght@700&display=swap" rel="stylesheet">
<style>
  :root {
    --brand-red: #ec1f27;
    --ink: #2b2b2b;
    --panel-grey: #9a9a9a;
    --band-black: #1c1b1c;
    --page-bg: #e6e4e1;
    --paper: #ffffff;
  }
  * { box-sizing: border-box; margin: 0; padding: 0; }
  html, body { width: 1200px; height: 800px; overflow: hidden; }
  body {
    background: var(--page-bg);
    font-family: "Open Sans", Arial, sans-serif;
    color: var(--ink);
  }
  .poster {
    position: absolute;
    left: 330px; top: 18px;
    width: 540px; height: 764px;
    background: linear-gradient(#fff 60%, #eeeeee 85%, #fff);
    overflow: hidden;
    box-shadow: 0 6px 18px rgba(0,0,0,.18);
  }
  .hero-photo {
    position: absolute; left: 0; top: 0;
    width: 540px; height: 360px;
    background: linear-gradient(135deg, #e9e7e4 0%, #d8d2cc 40%, #b9b3ae 70%, #f2f1ef 100%);
  }
  .title-banner {
    position: absolute; left: 0; top: 350px;
    width: 260px; height: 42px;
    background: linear-gradient(var(--brand-red), #c8161d);
    display: flex; align-items: center; padding-left: 26px;
  }
  .title-banner h1 {
    font-family: "Roboto Slab", Georgia, serif;
    font-weight: 700; font-size: 15px; color: #fff; letter-spacing: .2px;
    white-space: nowrap;
  }
  .intro {
    position: absolute; left: 26px; top: 408px; width: 240px;
    font-size: 10.2px; line-height: 1.3;
  }
  .intro p { margin-bottom: 9px; }
  .intro p.justified { text-align: justify; }
  .product { color: var(--brand-red); font-weight: 700; }
  .facts-panel {
    position: absolute; left: 282px; top: 350px;
    width: 240px; height: 270px;
    background: linear-gradient(#8e8e8e, #a3a3a3);
    border-radius: 12px;
    padding: 18px 14px;
    color: #f4f4f4; font-size: 10.2px; line-height: 1.3;
  }
  .facts-panel p { margin-bottom: 12px; }
  .facts-panel strong { font-weight: 700; }
  .contact-band {
    position: absolute; left: 0; bottom: 0;
    width: 540px; height: 108px;
    background: var(--band-black);
    display: flex; align-items: center;
    padding: 0 14px 0 30px;
  }
  .brand-name {
    display: flex; align-items: center; gap: 8px;
    font-size: 32px; font-weight: 400; color: #ffffff;
    letter-spacing: -.5px;
    width: 206px; flex-shrink: 0;
  }
  .brand-dot {
    width: 11px; height: 11px; background: var(--brand-red);
  }
  .contact-details {
    color: #ffffff; font-size: 12.8px; line-height: 1.3;
    white-space: nowrap;
  }
</style>
</head>
<body>
  <article class="poster">
    <div class="hero-photo" role="img" aria-label="Photo of two smiling women in striped tops sitting together holding mugs"></div>

    <div class="title-banner"><h1>Laser Vaginal Rejuvenation</h1></div>

    <section class="intro">
      <p>Have you ever laughed, coughed or sneezed and almost lost control of your bladder? This is known as incontinence. Clearview offers Seaton's only safe, fast and effective Stress Urinary Incontinence (SUI) or Light Bladder Leakage (LBL) laser treatment, called <span class="product">ContiLux™</span>.</p>
      <p class="justified">Many Australians, both men and women, suffer from incontinence but it is known to be a predominantly female condition. It is estimated that one out of four women over the age of 18 will have at least one episode of incontinency in their lifetime. Incontinency can be the result of weakened pelvic floor muscles, childbirth problems or degenerative changes associated with ageing.</p>
    </section>

    <aside class="facts-panel">
      <p>A specifically designed Solvane laser is inserted into the vagina to gently tighten, strengthen, firm, and lift the vaginal wall.</p>
      <p>70% of patients are dry after 120 days, with 98% of all patients reporting improvement. The treatment is safe with no adverse effects reported in any studies.</p>
      <p>a natural part of aging or the birth of a child, the pelvic floor will begin to relax and ongoing maintenance treatments may be required.</p>
      <p><strong>ContiLux™</strong> is virtually painless and has been designed to work quickly and safely with minimal discomfort. Usually only 2 treatments are required for great results.</p>
    </aside>

    <footer class="contact-band">
      <div class="brand-name"><span>clearview</span><span class="brand-dot"></span></div>
      <div class="contact-details">
        Suite 4-118 Harbour Rd., Seaton, QLD 4901<br>
        Phone (07) 5550 1234 | Fax (07) 5550 1299<br>
        clearviewclinic.example.com
      </div>
    </footer>
  </article>
</body>
</html>
```